Company Profile for Academic and Study Abroad Services

I am looking for Power Point Design for company Profile . the company is academic and study abroad services. you can visit the website which is www.brevolanta.ae . the colour i prefer is Dark Blue + White + Black . you can find all the content for power point and logo and some picture i need you to add it.

Target Market(s)

Students who wants to study abroad. Universities . Learning centre.

Industry/Entity Type

Education

Font styles to use
Serif
Sans Serif

Colors
0555a3
ffffff
000000
aaaaaa

Requirements
Must have
• Must Have Images for each slides.
Nice to have
• infographic. Images related to the study abroad

```html
<!DOCTYPE html>
<html lang="en">
<head>
<meta charset="utf-8">
<title>Brevolanta Company Profile Slides</title>
<link rel="stylesheet" href="https://fonts.googleapis.com/css2?family=Open+Sans:wght@400;600;700&display=swap">
<style>
  :root {
    --navy: #053c7f;
    --navy-deep: #042e63;
    --ring-blue: #0b1f9e;
    --white: #ffffff;
    --ink: #222222;
    --grey-dark: #5e5e62;
    --grey-mid: #858588;
    --grey-light: #f1f1f1;
    --grey-panel: #e3e3e3;
    --grey-rule: #e6e6e6;
    --stage: #6e6e6e;
  }
  * { box-sizing: border-box; margin: 0; padding: 0; }
  html, body { width: 1200px; height: 1200px; overflow: hidden; }
  body {
    background: var(--stage);
    font-family: "Open Sans", Arial, sans-serif;
    color: var(--ink);
    position: relative;
  }
  .slide {
    position: absolute;
    width: 413px;
    height: 302px;
    background: var(--white);
    overflow: hidden;
  }
  .slide--cover { left: 161px; top: 103px; }
  .slide--who { left: 627px; top: 103px; }
  .slide--what { left: 161px; top: 448px; }
  .slide--levels { left: 627px; top: 448px; }
  .slide--why { left: 161px; top: 793px; }
  .slide--destination { left: 627px; top: 793px; }

  .abs { position: absolute; }

  .brand {
    position: absolute;
    display: flex;
    align-items: center;
    gap: 3px;
    font-weight: 700;
    font-size: 7.5px;
    letter-spacing: 0.3px;
    color: var(--navy-deep);
  }
  .brand__mark { width: 6px; height: 6px; background: var(--navy-deep); }
  .slide .brand--corner { right: 14px; top: 24px; }

  .header-band {
    position: absolute;
    left: 0; top: 0;
    height: 56px;
    background: var(--navy);
    color: var(--white);
    font-size: 14.5px;
    font-weight: 400;
    display: flex;
    align-items: center;
    padding-left: 30px;
  }
  .slide-title {
    position: absolute;
    color: var(--navy);
    font-size: 14.5px;
    font-weight: 400;
  }
  .body-copy {
    font-size: 5.6px;
    line-height: 1.4;
    color: var(--ink);
  }
  .web-address {
    position: absolute;
    left: 18px; bottom: 15px;
    font-size: 9px;
    font-weight: 600;
    color: var(--navy-deep);
  }
  .foot-band {
    position: absolute;
    left: 0; bottom: 0;
    width: 100%; height: 11px;
    background: var(--navy-deep);
  }

  /* cover */
  .cover__photo {
    position: absolute; inset: 0;
    background: linear-gradient(100deg, #f4f0e6 0%, #e9e3d2 22%, #3b3a3c 38%, #2a2a2e 65%, #4a4440 100%);
  }
  .cover__logo-box {
    position: absolute; left: 0; top: 216px;
    width: 126px; height: 56px;
    background: var(--white);
  }
  .cover__logo-box .brand { left: 30px; top: 24px; }
  .cover__fold { position: absolute; left: 126px; top: 181px; }
  .cover__title-band {
    position: absolute; left: 176px; top: 216px;
    width: 237px; height: 56px;
    background: var(--navy);
    color: var(--white);
    font-weight: 700;
    font-size: 10.5px;
    line-height: 1.3;
    padding: 12px 0 0 22px;
  }

  /* who we are */
  .slide--who .header-band { width: 326px; }
  .who__chart { position: absolute; left: 0; top: 80px; }
  .who__copy { position: absolute; left: 24px; top: 260px; width: 370px; }

  /* what we do */
  .slide--what .header-band { width: 324px; }
  .service {
    position: absolute;
    top: 92px;
    width: 138px;
    text-align: center;
  }
  .service__icon {
    width: 54px; height: 54px;
    margin: 0 auto;
    border-radius: 50%;
    background: var(--grey-dark);
    display: flex; align-items: center; justify-content: center;
  }
  .service__title {
    margin-top: 12px;
    font-size: 9.5px;
    font-weight: 600;
    color: var(--grey-mid);
  }
  .service__panel {
    position: absolute;
    top: 191px; height: 97px;
    background: var(--grey-light);
    padding: 28px 22px 0 22px;
  }
  .service__panel--mid { background: var(--grey-panel); }

  /* education levels */
  .levels__photo {
    position: absolute; left: 23px; top: 76px;
    width: 165px; height: 109px;
    background: linear-gradient(180deg, #0d0d12 0%, #2a2a30 30%, #3f7a3a 55%, #4d8a40 70%, #9b2a2a 100%);
  }
  .levels__subtitle {
    position: absolute; left: 204px; top: 78px;
    font-size: 15px; color: var(--grey-mid);
  }
  .levels__copy { position: absolute; left: 204px; top: 104px; width: 140px; }

  /* why choose */
  .why__donut { position: absolute; left: 30px; top: 84px; }
  .bullet {
    position: absolute;
    display: flex; gap: 5px;
    width: 100px;
  }
  .bullet__dot {
    width: 3px; height: 3px; margin-top: 2px; flex: none;
    background: var(--ring-blue); transform: rotate(45deg);
  }
  .bullet__dot--soft { background: #cfd3e0; }
  .why__divider {
    position: absolute; left: 266px; top: 86px;
    width: 2px; height: 117px;
    background: var(--grey-rule);
  }
  .why__copy { position: absolute; left: 296px; top: 84px; width: 98px; }

  /* study destination */
  .slide--destination .header-band { width: 315px; }
  .destination__photo {
    position: absolute; left: 0; top: 60px;
    width: 413px; height: 114px;
    background: linear-gradient(90deg, #efe8e0 0%, #d9cdbf 35%, #b8a48e 55%, #8a7867 75%, #d8cec6 100%);
  }
  .destination__icons {
    position: absolute; left: 0; top: 179px;
    width: 413px; height: 32px;
    display: flex;
  }
  .destination__cell {
    flex: 1;
    display: flex; align-items: center; justify-content: center;
    background: var(--grey-dark);
  }
  .destination__cell--light { background: var(--grey-mid); }
  .destination__panel {
    position: absolute; left: 0; top: 211px;
    width: 413px; height: 77px;
    background: var(--grey-light);
    display: flex;
  }
  .destination__text { flex: 1; padding: 12px 18px 0 18px; }
</style>
</head>
<body>

  <!-- Cover -->
  <section class="slide slide--cover">
    <div class="cover__photo" role="img" aria-label="Group photo of smiling university students sitting together on a staircase"></div>
    <svg class="cover__fold" width="60" height="91" viewBox="0 0 60 91">
      <polygon points="0,35 24,0 60,0 60,91 0,91" fill="#8e8e92"/>
      <polygon points="24,0 50,0 50,35 24,35" fill="#6a6a70"/>
    </svg>
    <div class="cover__logo-box">
      <div class="brand"><span class="brand__mark"></span>BREVOLANTA</div>
    </div>
    <div class="cover__title-band">BREVOLANTA<br>Universities Entrance Services</div>
  </section>

  <!-- Who we are -->
  <section class="slide slide--who">
    <div class="header-band">WHO WE ARE</div>
    <div class="brand brand--corner"><span class="brand__mark"></span>BREVOLANTA</div>
    <svg class="who__chart" width="413" height="170" viewBox="0 0 413 170">
      <g stroke="#e8e8e8" stroke-width="1">
        <line x1="0" y1="13" x2="413" y2="13"/>
        <line x1="0" y1="31" x2="413" y2="31"/>
        <line x1="0" y1="49" x2="413" y2="49"/>
        <line x1="0" y1="67" x2="413" y2="67"/>
        <line x1="0" y1="85" x2="413" y2="85"/>
        <line x1="0" y1="103" x2="413" y2="103"/>
        <line x1="0" y1="121" x2="413" y2="121"/>
        <line x1="0" y1="139" x2="413" y2="139"/>
        <line x1="0" y1="157" x2="413" y2="157"/>
      </g>
      <rect x="31" y="40" width="3" height="120" fill="#6a6a70"/>
      <polygon points="46,160 111,47 181,160" fill="#5e5e62"/>
      <polygon points="219,160 291,85 378,160" fill="#5e5e62"/>
      <polygon points="138,160 180,85 223,160" fill="#8a8a8e"/>
    </svg>
    <p class="who__copy body-copy">We guide students from first enquiry to enrolment, matching every learner with programmes and universities that suit their goals and budget.</p>
  </section>

  <!-- What we do -->
  <section class="slide slide--what">
    <div class="header-band">WHAT WE DO</div>
    <div class="brand brand--corner"><span class="brand__mark"></span>BREVOLANTA</div>

    <div class="service" style="left:0;">
      <div class="service__icon">
        <svg width="24" height="24" viewBox="0 0 24 24" fill="none" stroke="#fff" stroke-width="1.6">
          <circle cx="14" cy="10" r="6"/><line x1="9.5" y1="14.5" x2="4" y2="20"/>
        </svg>
      </div>
      <div class="service__title">SAMPLE TITLE</div>
    </div>
    <div class="service" style="left:138px;">
      <div class="service__icon">
        <svg width="24" height="24" viewBox="0 0 24 24" fill="none" stroke="#fff" stroke-width="1.6">
          <path d="M16 7.5c-1-1.5-7-2-7 1.5s7 2 7 5.5-6 3-7.5 1"/><line x1="12" y1="3" x2="12" y2="21"/>
        </svg>
      </div>
      <div class="service__title">SAMPLE TITLE</div>
    </div>
    <div class="service" style="left:275px;">
      <div class="service__icon">
        <svg width="24" height="24" viewBox="0 0 24 24" fill="#fff">
          <rect x="6" y="13" width="3" height="6"/><rect x="11" y="8" width="3" height="11"/><rect x="16" y="15" width="3" height="4"/>
        </svg>
      </div>
      <div class="service__title">SAMPLE TITLE</div>
    </div>

    <div class="service__panel" style="left:0; width:134px;">
      <p class="body-copy">Course search across trusted partner universities worldwide.</p>
    </div>
    <div class="service__panel service__panel--mid" style="left:134px; width:135px;">
      <p class="body-copy">Fee planning, scholarship advice and clear cost breakdowns for each option we propose to families.</p>
    </div>
    <div class="service__panel" style="left:269px; width:144px;">
      <p class="body-copy">Progress tracking for every application, with regular updates.</p>
    </div>
  </section>

  <!-- Education levels -->
  <section class="slide slide--levels">
    <h2 class="slide-title" style="left:24px; top:18px;">EDUCATION LEVELS</h2>
    <div class="brand brand--corner"><span class="brand__mark"></span>BREVOLANTA</div>
    <div class="levels__photo" role="img" aria-label="Floodlit university sports stadium at night"></div>
    <div class="levels__subtitle">TEXT TITLE</div>
    <p class="levels__copy body-copy">Foundation, diploma, bachelor and master programmes, each explained with entry requirements, durations and typical intakes for the coming academic year.</p>
    <div class="web-address">www.brevolanta.ae</div>
    <div class="foot-band"></div>
  </section>

  <!-- Why choose -->
  <section class="slide slide--why">
    <h2 class="slide-title" style="left:29px; top:20px;">WHY CHOOSE BREVOLANTA</h2>
    <div class="brand brand--corner"><span class="brand__mark"></span>BREVOLANTA</div>
    <svg class="why__donut" width="110" height="110" viewBox="0 0 110 110">
      <defs>
        <radialGradient id="donut-core" cx="0.4" cy="0.4" r="0.7">
          <stop offset="0" stop-color="#e6f2f6"/>
          <stop offset="1" stop-color="#c9dfe6"/>
        </radialGradient>
      </defs>
      <circle cx="55" cy="55" r="45" fill="none" stroke="#ececee" stroke-width="10"/>
      <circle cx="55" cy="55" r="45" fill="none" stroke="var(--ring-blue)" stroke-width="10"
              stroke-dasharray="155 283" transform="rotate(-90 55 55)"/>
      <circle cx="55" cy="55" r="30" fill="url(#donut-core)"/>
    </svg>
    <div class="bullet" style="left:140px; top:86px;">
      <span class="bullet__dot"></span>
      <p class="body-copy">Personal advisers who know each campus well</p>
    </div>
    <div class="bullet" style="left:140px; top:181px;">
      <span class="bullet__dot"></span>
      <p class="body-copy">Fast offer letters from partner universities</p>
    </div>
    <div class="bullet" style="left:38px; top:216px;">
      <span class="bullet__dot bullet__dot--soft"></span>
      <p class="body-copy">Trusted since day one</p>
    </div>
    <div class="why__divider"></div>
    <p class="why__copy body-copy">Over a decade of admissions experience, a wide partner network and honest guidance mean students apply with confidence and arrive ready to succeed in their new country.</p>
    <div class="web-address">www.brevolanta.ae</div>
    <div class="foot-band"></div>
  </section>

  <!-- Study destination -->
  <section class="slide slide--destination">
    <div class="header-band">STUDY DESTINATION</div>
    <div class="brand brand--corner"><span class="brand__mark"></span>BREVOLANTA</div>
    <div class="destination__photo" role="img" aria-label="Portrait photo of a speaker in traditional Gulf dress"></div>
    <div class="destination__icons">
      <div class="destination__cell">
        <svg width="16" height="16" viewBox="0 0 16 16" fill="none" stroke="#fff" stroke-width="1.2">
          <circle cx="8" cy="5" r="3"/><path d="M2 15c0-3.5 3-5 6-5s6 1.5 6 5z"/>
        </svg>
      </div>
      <div class="destination__cell destination__cell--light">
        <svg width="18" height="16" viewBox="0 0 18 16" fill="none" stroke="#fff" stroke-width="1.2">
          <polyline points="1,1 1,15 17,15"/><polyline points="3,12 7,7 10,10 16,3"/>
        </svg>
      </div>
      <div class="destination__cell">
        <svg width="14" height="16" viewBox="0 0 14 16" fill="none" stroke="#fff" stroke-width="1.2">
          <path d="M7 1a4.5 4.5 0 0 0-2.5 8.2V11h5V9.2A4.5 4.5 0 0 0 7 1z"/><line x1="5" y1="13" x2="9" y2="13"/><line x1="5.5" y1="15" x2="8.5" y2="15"/>
        </svg>
      </div>
      <div class="destination__cell destination__cell--light">
        <svg width="16" height="16" viewBox="0 0 16 16" fill="none" stroke="#fff" stroke-width="1.2">
          <circle cx="8" cy="8" r="6.5"/><polyline points="9.5,5 6.5,8 9.5,11"/>
        </svg>
      </div>
    </div>
    <div class="destination__panel">
      <p class="destination__text body-copy">Visa support and document checks for every student.</p>
      <p class="destination__text body-copy">Rankings and outcomes compared across countries.</p>
      <p class="destination__text body-copy">Ideas for cities that match student life goals.</p>
      <p class="destination__text body-copy">Intake dates planned well ahead of deadlines.</p>
    </div>
  </section>

</body>
</html>
```